Business card for Northland's Blue Wagon.

Good day i am looking for a business card design for my business.
The name of the business is Northland's Blue Wagon. It is a van rental business that provides a driver and helper to the customer. Customer have use to van for small moves, studio or 1 bedroom, Moving furniture like couch or kitchen cabinets.
We are available evenings, weekends and holidays.
the means to contact us is by phone at 628-947-2071; By emails at Oakridge@northlandsbluewagon.net; or by social media, Facebook and Instagram.
You can see attached pictures of the van and or logo.

```html
<!DOCTYPE html>
<html lang="en">
<head>
<meta charset="utf-8">
<title>Northland's Blue Wagon – Business Card</title>
<link href="https://fonts.googleapis.com/css2?family=Cinzel:wght@700&family=Michroma&family=Orbitron:wght@700;800&family=Roboto:wght@400;700&display=swap" rel="stylesheet">
<style>
  :root {
    --backdrop: #737373;
    --brand-red: #d30000;
    --deep-red: #a80000;
    --paper: #f6f5f3;
    --ink: #111111;
    --white: #ffffff;
    --ghost: rgba(0,0,0,0.07);
  }
  * { margin: 0; padding: 0; box-sizing: border-box; }
  html, body { width: 1200px; height: 1000px; overflow: hidden; }
  body { background: var(--backdrop); position: relative; font-family: "Roboto", Arial, sans-serif; }

  .card {
    position: absolute;
    left: 294px;
    width: 613px;
    height: 351px;
    overflow: hidden;
    box-shadow: 14px 16px 22px rgba(0,0,0,0.35);
  }

  /* Front */
  .card-front { top: 142px; background: var(--brand-red); }
  .front-mark {
    position: absolute;
    left: 0; right: 0; top: 150px;
    text-align: center;
    font-family: "Cinzel", Georgia, serif;
    font-weight: 700;
    font-size: 34px;
    color: var(--deep-red);
  }
  .social-line {
    position: absolute;
    left: 0; right: 0; top: 310px;
    display: flex;
    justify-content: center;
    align-items: center;
    gap: 6px;
    color: var(--white);
    font-weight: 700;
    font-size: 13px;
  }
  .social-dot { width: 16px; height: 16px; border-radius: 50%; background: var(--white); }

  /* Back */
  .card-back { top: 516px; background: var(--paper); }
  .back-ghost-mark {
    position: absolute;
    left: 300px; top: 200px;
    font-family: "Cinzel", Georgia, serif;
    font-weight: 700;
    font-size: 70px;
    white-space: nowrap;
    color: var(--ghost);
  }
  .corner-mark {
    position: absolute;
    left: 40px; top: 34px;
    width: 112px;
    display: flex;
    align-items: center;
    gap: 6px;
  }
  .corner-mark-dot { flex: none; width: 22px; height: 22px; border-radius: 50%; background: var(--brand-red); }
  .corner-mark-name {
    font-family: "Cinzel", Georgia, serif;
    font-weight: 700;
    font-size: 12px;
    line-height: 1.2;
    color: var(--brand-red);
  }
  .business-name {
    position: absolute;
    left: 166px; top: 62px;
    font-family: "Cinzel", Georgia, serif;
    font-weight: 700;
    font-size: 26px;
    color: var(--brand-red);
    white-space: nowrap;
  }
  .tagline {
    position: absolute;
    left: 0; width: 604px; top: 170px;
    text-align: center;
    font-family: "Michroma", Arial, sans-serif;
    font-weight: 700;
    font-size: 21px;
    color: var(--ink);
    -webkit-text-stroke: 0.6px var(--ink);
  }
  .hours-band {
    position: absolute;
    left: 154px; width: 308px; top: 252px; height: 22px;
    background: linear-gradient(90deg, rgba(0,0,0,0) 0%, #000 18%, #000 82%, rgba(0,0,0,0) 100%);
    color: var(--white);
    font-weight: 700;
    font-size: 14px;
    text-align: center;
    line-height: 22px;
    letter-spacing: 0.3px;
  }
  .phone {
    position: absolute;
    left: 0; width: 616px; top: 274px;
    text-align: center;
    font-family: "Orbitron", Arial, sans-serif;
    font-weight: 800;
    font-size: 30px;
    color: var(--brand-red);
    letter-spacing: 1px;
  }
  .email {
    position: absolute;
    left: 0; width: 616px; top: 307px;
    text-align: center;
    font-size: 15px;
    color: var(--ink);
  }
</style>
</head>
<body>
  <section class="card card-front">
    <div class="front-mark">Northland's Blue Wagon</div>
    <div class="social-line">
      <span class="social-dot"></span>
      <span class="social-handle">northlandsbluewagon</span>
    </div>
  </section>

  <section class="card card-back">
    <div class="back-ghost-mark" aria-hidden="true">Northland's Blue Wagon</div>
    <div class="corner-mark">
      <span class="corner-mark-dot"></span>
      <span class="corner-mark-name">Northland's Blue Wagon</span>
    </div>
    <h1 class="business-name">Northland's Blue Wagon</h1>
    <p class="tagline">Your friend with the van</p>
    <p class="hours-band">evenings • weekends • holidays</p>
    <p class="phone">628-947-2071</p>
    <p class="email">oakridge@northlandsbluewagon.net</p>
  </section>
</body>
</html>
```